Flyer-Design für Onlineshop für italienische Naturkosmetik
Zielgruppe
Onlineshop für italienische Naturkosmetik aus der Toskana (https://www.lavendo-seifenhaus.com), Zielgruppe Frauen 30+ mit Interesse vegane Lebensweise, Reiseland Italien und naturverbunden
Aufgabenstellung
Benötigt wird ein Paketbeileger beidseitig bedruckt, mit Gutschein wahlweise im Format DIN lang plus (10,5 x 21 cm) oder DIN lang (9,8 x 21 cm). Passende Texte können von der Webseite übernommen werden, zB. Startseite unten.
Die Beileger werden über Versender italienischer Feinkost verteilt. Insofern sind die Empfänger genauso italophil, wie es unsere Zielgruppe auch ist. Naturkosmetik setzen wir gleich mit handmade, kleinen familiengeführten Manufakturen, besten Rohstoffen aus der Region (Olivenöl, Kräuter, Duftöle)
Emotionale Bildsprache, klare Auslobung des Angebots, vertrauensbildende Vorteile (Zertifikate, Bewertungen, Awards). Einige Produkte im Shop wurden 2015 bereits mit dem Glanzfeder Beauty Award ausgezeichnet.

```html
<!DOCTYPE html>
<html lang="de">
<head>
<meta charset="utf-8">
<title>Lavendo Seifenhaus – Gutschein</title>
<link rel="stylesheet" href="https://fonts.googleapis.com/css2?family=Playfair+Display:wght@400;600&display=swap">
<style>
  :root {
    --stage: #c8c9cc;
    --band: #e6efc9;
    --band-text: #4e6a1e;
    --badge: rgba(128, 178, 62, 0.94);
    --brand: #6f9f2c;
    --white: #ffffff;
    --frame: rgba(255, 255, 255, 0.85);
    --wood: #d2cdc2;
  }
  * { margin: 0; padding: 0; box-sizing: border-box; }
  html, body {
    width: 1200px;
    height: 675px;
    overflow: hidden;
    background: var(--stage);
  }
  .voucher {
    position: absolute;
    left: 11px;
    top: 81px;
    width: 1172px;
    height: 546px;
    overflow: hidden;
    font-family: "Playfair Display", Georgia, serif;
  }
  .scene {
    position: absolute;
    left: 0; top: 0;
    width: 1172px;
    height: 472px;
    background: linear-gradient(180deg, #d8d3c8 0%, var(--wood) 50%, #dcd7cc 100%);
  }
  .scene__flowers {
    position: absolute;
    left: 0; top: 0;
    width: 340px;
    height: 472px;
    background:
      radial-gradient(ellipse 120px 150px at 170px 270px, rgba(250, 250, 244, 0.9), transparent 75%),
      radial-gradient(ellipse 140px 120px at 200px 40px, rgba(248, 248, 240, 0.75), transparent 75%),
      linear-gradient(90deg, #4f8033 0%, #6f9a4d 45%, rgba(160, 180, 140, 0.6) 80%, transparent 100%);
  }
  .scene__bottles {
    position: absolute;
    left: 295px; top: 70px;
    width: 150px;
    height: 190px;
    border-radius: 40%;
    background: radial-gradient(ellipse at center, rgba(40, 30, 25, 0.55), transparent 70%);
  }
  .scene__scoop {
    position: absolute;
    left: 430px; top: 0;
    width: 370px;
    height: 150px;
    background: radial-gradient(ellipse 190px 80px at 50% 20%, rgba(150, 110, 70, 0.45), transparent 75%);
  }
  .scene__products {
    position: absolute;
    right: 0; top: 0;
    width: 380px;
    height: 472px;
    background:
      radial-gradient(ellipse 90px 110px at 130px 90px, rgba(250, 250, 246, 0.95), transparent 80%),
      radial-gradient(ellipse 110px 160px at 260px 240px, rgba(238, 222, 175, 0.9), transparent 80%),
      radial-gradient(ellipse 150px 110px at 250px 420px, rgba(248, 248, 240, 0.9), transparent 80%),
      radial-gradient(ellipse 70px 100px at 370px 430px, rgba(80, 130, 50, 0.8), transparent 80%);
  }
  .scene__glow {
    position: absolute;
    left: 385px; top: 75px;
    width: 390px;
    height: 385px;
    border-radius: 50%;
    background: radial-gradient(circle, rgba(255, 255, 255, 0.6) 55%, transparent 72%);
  }

  .voucher__frame-line {
    position: absolute;
    background: var(--frame);
  }
  .voucher__frame-line--top { left: 37px; top: 67px; width: 774px; height: 1.5px; }
  .voucher__frame-line--left { left: 37px; top: 67px; width: 1.5px; height: 405px; }
  .voucher__frame-line--right { left: 1108px; top: 119px; width: 1.5px; height: 353px; }

  .offer-badge {
    position: absolute;
    left: 415px;
    top: 103px;
    width: 329px;
    height: 329px;
    border-radius: 50%;
    overflow: hidden;
    background: var(--badge);
    color: var(--white);
    text-align: center;
  }
  .offer-badge__line {
    position: absolute;
    left: 0; right: 0;
    font-size: 55px;
    font-weight: 400;
    line-height: 1;
  }
  .offer-badge__line--title { top: 68px; }
  .offer-badge__line--value { top: 134px; }
  .offer-badge__line--for { top: 199px; }
  .offer-badge__sprig {
    position: absolute;
    top: 190px;
    width: 96px;
    height: 110px;
    background: rgba(255, 255, 255, 0.16);
    border-radius: 50% 50% 50% 50% / 60% 60% 40% 40%;
  }
  .offer-badge__sprig--left { left: 14px; transform: rotate(-30deg); }
  .offer-badge__sprig--right { right: 14px; transform: rotate(30deg); }

  .brand {
    position: absolute;
    left: 842px;
    top: 20px;
    display: flex;
    align-items: center;
    gap: 12px;
    color: var(--brand);
    font-weight: 600;
  }
  .brand__dot {
    width: 56px;
    height: 56px;
    border-radius: 50%;
    background: var(--brand);
  }
  .brand__name {
    font-size: 37px;
    line-height: 1.05;
  }

  .redeem-band {
    position: absolute;
    left: 0; top: 472px;
    width: 1172px;
    height: 74px;
    background: var(--band);
    display: flex;
    align-items: center;
    justify-content: center;
    gap: 10px;
    padding: 0 22px;
  }
  .redeem-band__rule {
    flex: 1;
    height: 1.5px;
    background: var(--band-text);
  }
  .redeem-band__text {
    color: var(--band-text);
    font-size: 32px;
    font-weight: 400;
    white-space: nowrap;
    padding: 0 4px 4px;
  }
</style>
</head>
<body>
  <main class="voucher">
    <div class="scene" role="img" aria-label="Foto: heller Holztisch mit Badesalz, Jasminblüten, Duftölfläschchen, Holzschaufel, Kräuterstempeln und Naturseife">
      <div class="scene__flowers"></div>
      <div class="scene__bottles"></div>
      <div class="scene__scoop"></div>
      <div class="scene__products"></div>
      <div class="scene__glow"></div>
    </div>
    <span class="voucher__frame-line voucher__frame-line--top"></span>
    <span class="voucher__frame-line voucher__frame-line--left"></span>
    <span class="voucher__frame-line voucher__frame-line--right"></span>

    <div class="brand">
      <span class="brand__dot"></span>
      <span class="brand__name">Lavendo<br>Seifenhaus</span>
    </div>

    <section class="offer-badge">
      <span class="offer-badge__sprig offer-badge__sprig--left" role="img" aria-label="Gezeichneter Olivenzweig"></span>
      <span class="offer-badge__sprig offer-badge__sprig--right" role="img" aria-label="Gezeichneter Olivenzweig"></span>
      <p class="offer-badge__line offer-badge__line--title">Gutschein</p>
      <p class="offer-badge__line offer-badge__line--value">XX €</p>
      <p class="offer-badge__line offer-badge__line--for">für</p>
    </section>

    <footer class="redeem-band">
      <span class="redeem-band__rule"></span>
      <p class="redeem-band__text">Jetzt einlösen unter www.lavendo-seifenhaus.com</p>
      <span class="redeem-band__rule"></span>
    </footer>
  </main>
</body>
</html>
```